Graphic Design Project for Product Package

Dr. Lorenz Wimbacher Naturprodukte VERANOL®, a small family-run “start-up” business (has been around since mid 90s but only now beginning to focus efforts on growth), wishes to redesign its entire line of packaging graphics, beginning with the cardboard box for its Black Mud Powder from the Dead Sea.

Our company is based in Austria and is specializes in the production of organic cosmetics in the mid-upper pricing range. We pride ourselves in offering natural cosmetics (the meaning of “natural” is relative and each person may have a different definition), with no petrochemical preservatives. Some of our products, such as the mineral salts and black mud powder from the Dead Sea cannot be obtained more naturally, unless you actually visit the area, thus retain all their properties. Our products are not medicine but the basic Dead Sea ingredients are used by spas and clinics in the area to treat various different skin, joint and bone affections. Our male and female customers (no distinction made!), primarily as of the ages of 18 to 65, buy VERANOL® because they:

• Care about the exterior and interior well-being
• Wish to look well cared, preserve their skin’s flexibility, natural splendor & properties
• Prefer natural skin care
• Nourish their skin with vital minerals/trace elements, protecting/treating their skin with natural ingredients
• Willing to pay more than average for natural cosmetics, looking for quality,
• Don’t mind spending about 15 minutes per week preparing a mud mask with some hot water.
• Know or are surprised to find out that Dead Sea mud is one of the few, if not the only, naturally astringent (tenses the skin) muds in the world
• Help alleviate skin conditions (e.g. psoriasis, dermatitis, acne, eczema, pustules, oily skin ...), joint (e.g. rheumatism, arthritis ...) and cardiovascular disease.

The black mud powder and mineral salts both contain sulfur and zinc, two naturally disinfecting and healing minerals, thus their common use in many dermatological drugs. Both salts and mud are natural and without chemicals, which is important when dealing with sensitive or problematic skin, which reacts allergically to certain types of substances. Many of the competitors creams today use common ingredients such as petrolatum, paraffin (paraffinum liquidum), mineral oil, among others, which are derived from oil, are cheap ingredients (higher margins!) and clog pores!

To underline that this is not a chimera, there are quite a few researchers/scientists/doctors who have written articles about the benefits of the Dead Sea. Below are some links to abstracts of research papers, which are helpful in understanding the therapeutic potential of the black mud powder:

http://library.examplepress.test/doi/10.1111/a.1001-2001.1995.aa00001.x/abstract
http://library.examplepress.test/doi/10.1111/a.1001-2002.2005.aa00002.x/full
http://library.examplepress.test/doi/10.1046/a.1001-2001.1997.aa00003.x/abstract
http://rhj.medjournal.test/content/12/3/45.short
http://www.scholarhub.test/content/qx12a3b4c5d6e789/
http://library.examplepress.test/doi/10.1111/a.1001-2002.2005.aa00004.x/full
http://periodicals.medhouse.test/jointres/Abstract/2002/08000/Clay_Wraps_Trial_Article.3.aspx
http://library.examplepress.test/doi/10.1111/a.1003-3003.1997.aa00005.x/abstract
http://library.examplepress.test/doi/10.1046/a.1004-4004.2003.aa00006.x/full
http://library.examplepress.test/doi/10.1046/a.1001-2001.1999.aa00007.x/full

The following links lead you to VERANOL® product data, mineral characteristics and a video of how to prepare a facial mud mask:

http://www.veranol7.test/descargaanalisis.htm
http://www.veranol7.test/estudio.htm
http://www.clipstream.test/watch?v=Kq8wZpLm3Tx

We would like to convey, through our striking and attractive new package graphic design, our values to potential clients: quality, 100% natural product, effectiveness, seriousness, confidence, respect for the environment, people, animals (the products are not tested on animals), all of which has a price (they are not cheap!).

So far we have 3 languages on the boxes / labels: German, Spanish and English (a 4th language will be included). We are looking for a graphic design that will communicate our values and captivate people's attention, thereby helping us increase sales, projecting an image of reliability, effectiveness and trust. Although we are not, and do not wish to, market our products as medicine, we do want to express, through our new graphic design, the fact that these products can be used to treat all types of skin, mitigate certain skin affections, and, depending on each organism’s reaction, different ailments, although they won’t cure them (they can alleviate!).

To get an idea of our company, I invite you to explore our website, www.veranol7.test, and see photos of our products. Attached please find the photo of the black mud powder box 100 grams. We would like to keep the entire line with a similar design to create a unified brand image. At this point we know that some, if not all, packages do not convey quality nor our values – this is something we wish to gradually change as each products’ graphic design and packaging gets renewed, consistent with the new brand image. This is work-in-progress and will be addressed as the company grows and has the financial capacity to invest in new design and packaging. We are advancing step by step, starting with the re-design of our 100 grams box of black mud powder.

We think that the thickness of the cardboard box (the thicker, the better the quality?), the exterior and interior box colors, and texts used, are key. Today palms are associated with other images (although design/packaging is an important element in cosmetics, it must convey the right messages; palm trees are associated with desert, dry climate, perhaps vacation, food…), and do not necessarily transmit our values nor the product’s characteristics. In addition, there is too much tiny text on the back, making it unreadable. Therefore, we believe there is a need to remove the palm trees and reduce the amount of text, to an easily legible format. Two colors are being currently used, green Pantone No. 326 and blue Pantone No. 072. We would be happy to change these if the desired goals are more easily met.

In that sense, we are looking for someone to help us with our packaging graphic design (in later projects, also packaging), that would encompass also placing and formatting the text on the backside of the box, with an affordable budget. If the designer suffers from skin diseases, circulatory or joint, we could also consider a payment in kind (preferential prices), which would be ideal but not essential. At some point we hope to have more budget (ideally because the new graphic design has helped us grow) and then we will try to continue renewing the rest of the VERANOL® line.

We hope you find the project interesting. Any questions, please do not hesitate to contact us. Thank you very much for your time, recommendations and proposals. Ideally we can close this project in maximum 10-14 days.

Information to be considered and/or included in the design:

Box dimensions (all data in cm):

Front and back side: 6.5 x 8.2
Lateral sides: 3.3 x 8.2
Top & bottom sides: 3.3 x 6.5

Net weight: 100 g / 3.5 oz

Hi,

We have just guaranteed the project.

Regards,
Tobias

Target Market(s)

Male & female customers, approx. age 18-65, who care about their exterior and interior well being, “worried” about their skin, willing to pay more tha

Industry/Entity Type

Graphic Design

Requirements
Must have
• 1) Please consider approximate box/package dimensions (all data in cm):

Lateral sides: 3.3 x 8.2

2) Text to be included somewhere on the box:

3) VERANOL® Logo

4) Text to be included on the back side of the box:

VERANOL® Mineralschlammpulver aus den Tiefen des Toten Meeres ist ein Naturprodukt allergrößter Reinheit. Auf die Haut aufgetragen ist VERANOL® Mineralschlamm der reinste Balsam bei Hautirritationen, Verspannungen, aber auch eine entspannende Erholung für den ganzen Körper. Zur porentiefen Reinigung des Dermis, hautstraffend, entfernt problemlos tote Hautzellen und Unreinheiten. Verringert Anzeichen von Stress und Müdigkeit. Versorgt Ihre Haut mit Mineralien des Toten Meeres, notwendig für eine gesunde, jung ausschauende Haut. Der Inhalt dieser Packung ergibt ca. 140 ml und ist ausreichend für bis zu 15 Anwendungen. Siehe Packungsbeilage mit ausführlichen Gebrauchshinweisen.

VERANOL® Black Mud Powder, derived from the depths of the Dead Sea, is a natural, unspoiled product rich in skin-nourishing minerals. Applied to skin, it soothes dermis irritations, relieves stiffness, among others. For deep cleansing of the dermis, eliminates instantly dead skin cells and impurities smoothening the skin. Reduces stress and fatigue appearances, supplies your epidermis with vital Dead Sea minerals indispensible for a healthy, young-looking skin.
See package insert with detailed usage instructions.

El VERANOL® Barro Negro Mineral en polvo es extraído de las profundidades del Mar Muerto, siendo por ésta razón un producto totalmente natural y eficaz para el cuidado y limpieza de la piel. Aplicándola sobre la piel, el lodo mineral resulta un bálsamo perfecto contra las irritaciones cutáneas, tensiones y dolores de las articulaciones contribuyendo al mismo tiempo al relajamiento muscular y al bienestar general del cuerpo. Con la utilización del lodo mineral se consigue una limpieza profunda de la epidermis ya que elimina las impurezas y células muertas obteniendo así una piel tersa y lisa, los minerales que contiene el lodo nutren la piel de la forma que disminuyen las señales de cansancio y hacen que la piel recupere su luminosidad. Ver el prospecto con instrucciones detalladas para su uso.
INCI/Ingredients: LIMUS.
VERANOL® NATURPRODUKTE DR. LORENZ WIMBACHER
Lindenhofgasse 7, 3400 Ortshausen, Austria, www.veranol7.test, info@veranol7.test.
Should not have
• Should not have more than 5 colors.

```html
<!DOCTYPE html>
<html lang="de">
<head>
<meta charset="utf-8">
<title>VERANOL® Mineralschlammpulver – Faltschachtel 100 g</title>
<link href="https://fonts.googleapis.com/css2?family=Open+Sans:ital,wght@0,400;0,600;0,700;1,400&family=PT+Sans+Narrow:wght@400;700&display=swap" rel="stylesheet">
<style>
  :root{
    --navy:#1f2a5c;
    --navy-deep:#18224d;
    --ink-light:#ffffff;
    --tagline:#b9d0ef;
    --sky-top:#7e9fc4;
    --sky-low:#c9d8e6;
    --sea:#3fa0b4;
    --salt:#e8eef0;
    --page:#ffffff;
  }
  *{margin:0;padding:0;box-sizing:border-box}
  html,body{width:1200px;height:998px;overflow:hidden;background:var(--page)}
  body{position:relative;font-family:"Open Sans",Arial,sans-serif;color:var(--ink-light)}
  .panel{position:absolute;background:var(--navy);overflow:hidden}

  .flap-top{left:220px;top:60px;width:316px;height:204px}
  .flap-bottom{left:220px;top:736px;width:316px;height:204px}
  .side-left{left:36px;top:266px;width:180px;height:454px}
  .front{left:220px;top:266px;width:316px;height:454px}
  .side-right{left:574px;top:266px;width:180px;height:454px}
  .back{left:756px;top:266px;width:416px;height:454px;padding:18px 22px}

  .scene{position:absolute;left:0;top:0;width:100%;
    background:linear-gradient(180deg,var(--sky-top) 0%,var(--sky-low) 38%,var(--sea) 58%,var(--salt) 78%,var(--navy) 100%)}
  .side-left .scene,.side-right .scene{height:200px}
  .front .scene{height:520px;top:0;height:260px}

  .title{position:absolute;left:0;width:100%;text-align:center;text-shadow:0 1px 3px rgba(0,0,0,.35)}
  .title .main{display:block;font-weight:700;color:var(--ink-light)}
  .title .sub{display:block;font-style:italic;color:var(--ink-light)}
  .side-left .title,.side-right .title{top:58px}
  .side-left .main,.side-right .main{font-size:15px}
  .side-left .sub,.side-right .sub{font-size:13px;line-height:1.25}
  .front .title{top:30px}
  .front .main{font-size:25px}
  .front .sub{font-size:22px;line-height:1.25}

  .portrait{position:absolute;left:116px;top:162px;width:84px;height:84px;border-radius:50%;
    border:2px solid var(--ink-light);background:radial-gradient(circle at 50% 40%,#e6c9b4,#9fb7cf)}

  .tagline{position:absolute;left:0;width:100%;text-align:center;font-style:italic;color:var(--tagline);line-height:1.3}
  .side-left .tagline,.side-right .tagline{top:232px;font-size:12px}
  .front .tagline{top:278px;font-size:14px}

  .brand{position:absolute;left:0;width:100%;display:flex;align-items:center;justify-content:center;gap:6px;
    font-weight:700;color:var(--ink-light);letter-spacing:.5px}
  .brand .dot{width:12px;height:12px;border-radius:50%;background:var(--ink-light)}
  .side-left .brand,.side-right .brand{top:360px;font-size:13px}
  .front .brand{top:360px;font-size:15px}

  .net{position:absolute;left:0;top:92px;width:100%;text-align:center;font-size:12px;color:var(--ink-light)}

  .back-copy{font-family:"PT Sans Narrow",Arial,sans-serif;font-size:9.2px;line-height:1.18;color:var(--ink-light)}
  .back-copy p{margin-bottom:7px}
  .back-copy b{font-weight:700}
  .maker{position:absolute;left:22px;bottom:18px;font-family:"PT Sans Narrow",Arial,sans-serif;font-size:9.2px;line-height:1.2}
  .inci{position:absolute;right:22px;bottom:18px;font-family:"PT Sans Narrow",Arial,sans-serif;font-size:9.2px}
</style>
</head>
<body>

<div class="panel flap-top"></div>

<section class="panel side-left">
  <div class="scene" role="img" aria-label="Photo of the Dead Sea shore with white salt formations under a blue sky"></div>
  <h2 class="title"><span class="main">Mineralschlammpulver</span><span class="sub">Black Mud Powder</span><span class="sub">Lodo Mineral</span></h2>
  <p class="tagline">Natürliches Pflege-<br>Reinigungskosmetikum<br>für alle Hauttypen</p>
  <div class="brand"><span class="dot"></span>VERANOL®</div>
</section>

<section class="panel front">
  <div class="scene" role="img" aria-label="Photo of the Dead Sea shore with white salt formations under a blue sky"></div>
  <h1 class="title"><span class="main">Mineralschlammpulver</span><span class="sub">Black Mud Powder</span><span class="sub">Lodo Mineral</span></h1>
  <div class="portrait" role="img" aria-label="Round portrait photo of a person wearing a mud face mask"></div>
  <p class="tagline">Natürliches Pflege- Reinigungskosmetikum<br>für alle Hauttypen</p>
  <div class="brand"><span class="dot"></span>VERANOL®</div>
</section>

<section class="panel side-right">
  <div class="scene" role="img" aria-label="Photo of the Dead Sea shore with white salt formations under a blue sky"></div>
  <h2 class="title"><span class="main">Mineralschlammpulver</span><span class="sub">Black Mud Powder</span><span class="sub">Lodo Mineral</span></h2>
  <p class="tagline">Natürliches Pflege-<br>Reinigungskosmetikum<br>für alle Hauttypen</p>
  <div class="brand"><span class="dot"></span>VERANOL®</div>
</section>

<section class="panel back">
  <div class="back-copy">
    <p><b>VERANOL® Mineralschlammpulver</b> aus den Tiefen des Toten Meeres ist ein Naturprodukt allergrößter Reinheit. Auf die Haut aufgetragen ist VERANOL® Mineralschlamm der reinste Balsam bei Hautirritationen, Verspannungen, aber auch eine entspannende Erholung für den ganzen Körper. Zur porentiefen Reinigung des Dermis, hautstraffend, entfernt problemlos tote Hautzellen und Unreinheiten. Verringert Anzeichen von Stress und Müdigkeit. Versorgt Ihre Haut mit Mineralien des Toten Meeres, notwendig für eine gesunde, jung ausschauende Haut. Der Inhalt dieser Packung ergibt ca. 140 ml und ist ausreichend für bis zu 15 Anwendungen. Siehe Packungsbeilage mit ausführlichen Gebrauchshinweisen.</p>
    <p><b>VERANOL® Black Mud Powder</b>, derived from the depths of the Dead Sea, is a natural, unspoiled product rich in skin-nourishing minerals. Applied to skin, it soothes dermis irritations, relieves stiffness, among others. For deep cleansing of the dermis, eliminates instantly dead skin cells and impurities smoothening the skin. Reduces stress and fatigue appearances, supplies your epidermis with vital Dead Sea minerals indispensible for a healthy, young-looking skin. See package insert with detailed usage instructions.</p>
    <p><b>El VERANOL® Barro Negro Mineral en polvo</b> es extraído de las profundidades del Mar Muerto, siendo por ésta razón un producto totalmente natural y eficaz para el cuidado y limpieza de la piel. Aplicándola sobre la piel, el lodo mineral resulta un bálsamo perfecto contra las irritaciones cutáneas, tensiones y dolores de las articulaciones contribuyendo al mismo tiempo al relajamiento muscular y al bienestar general del cuerpo. Con la utilización del lodo mineral se consigue una limpieza profunda de la epidermis ya que elimina las impurezas y células muertas obteniendo así una piel tersa y lisa, los minerales que contiene el lodo nutren la piel de la forma que disminuyen las señales de cansancio y hacen que la piel recupere su luminosidad. Ver el prospecto con instrucciones detalladas para su uso.</p>
  </div>
  <address class="maker" style="font-style:normal">VERANOL® NATURPRODUKTE<br>DR. LORENZ WIMBACHER<br>Lindenhofgasse 7,<br>3400 Ortshausen, Austria<br><br><b>info@veranol7.test</b><br><b>www.veranol7.test</b></address>
  <p class="inci">INCI/Ingredients: LIMUS.</p>
</section>

<div class="panel flap-bottom"><p class="net">Net weight: 100 g / 3.5 oz</p></div>

</body>
</html>
```